Velisto Events Business Card

We need a business cards that stands out to our clients. We are company who targets prestige clients to spend money with us on experiences, so our image needs to be prestige
Target Market(s)
Corporate
Contact Information for Business Card
There will be four different names on the business cards
Dana Morrowby
Director
O: 02 5147 3086
M: 0451 692 038
E: info@velistoevents.example.au
Facebook: @velistoevents
Instagram: velistoevents
www.velistoevents.example.au
Nathaniel Morrowby
Director
O: 02 5147 3086
M: 0467 215 904
Facebook: @velistoevents
Instagram: velistoevents
www.velistoevents.example.au
Teodor Vinkel
Director
O: 02 5147 3086
M: 0478 903 527
Facebook: @velistoevents
Instagram: velistoevents
www.velistoevents.example.au
Mabel Hartung
Director
O: 02 5147 3086
Facebook: @velistoevents
Instagram: velistoevents
www.velistoevents.example.au
Colors
Designer to choose colors to be used in the design.
Look and feel

```html
<!DOCTYPE html>
<html lang="en">
<head>
<meta charset="utf-8">
<title>Velisto Events Business Card</title>
<link href="https://fonts.googleapis.com/css2?family=Arimo:wght@400;700&display=swap" rel="stylesheet">
<style>
  :root {
    --page: #2a2a2c;
    --navy: #11143f;
    --gold: #d8b14f;
    --gold-light: #f2d98a;
    --gold-deep: #b08a2a;
    --white: #ffffff;
  }
  * { box-sizing: border-box; margin: 0; padding: 0; }
  html, body { width: 1200px; height: 1108px; overflow: hidden; }
  body {
    background: var(--page);
    font-family: "Arimo", Arial, sans-serif;
    display: flex;
    justify-content: center;
    align-items: center;
    gap: 80px;
  }
  .card {
    position: relative;
    width: 420px;
    height: 680px;
    background: var(--navy);
    border-radius: 26px;
    overflow: hidden;
    color: var(--white);
  }
  .gold-band {
    position: absolute;
    left: 64px;
    right: 64px;
    height: 24px;
    background: linear-gradient(90deg, var(--gold-deep), var(--gold-light) 55%, var(--gold));
  }
  .gold-band--bottom { bottom: 0; border-radius: 24px 24px 0 0; }
  .gold-band--top { top: 0; border-radius: 0 0 24px 24px; }

  .wordmark {
    display: flex;
    align-items: center;
    justify-content: center;
    gap: 12px;
    color: var(--gold);
    font-weight: 400;
    font-size: 24px;
    letter-spacing: 6px;
    text-transform: uppercase;
    text-align: center;
    white-space: nowrap;
  }
  .wordmark__mark {
    width: 14px;
    height: 14px;
    background: var(--gold);
    flex: none;
  }

  .card--front .wordmark { margin-top: 110px; }
  .person { text-align: center; margin-top: 56px; }
  .person__name { font-size: 26px; font-weight: 700; }
  .person__role { font-size: 17px; color: var(--gold); margin-top: 2px; }

  .contact { width: 310px; margin: 22px auto 0; text-align: center; }
  .contact__item { padding: 12px 0; border-bottom: 1px solid var(--gold); }
  .contact__item:last-child { border-bottom: none; }
  .contact__label { font-size: 15px; font-weight: 700; color: var(--gold); }
  .contact__value { font-size: 17px; margin-top: 4px; line-height: 1.35; }

  .social {
    display: flex;
    align-items: center;
    gap: 8px;
    width: 310px;
    margin: 4px auto 0;
  }
  .social__rule { flex: 1; height: 1px; background: var(--gold); }
  .social__dot {
    width: 28px;
    height: 28px;
    border-radius: 50%;
    background: var(--gold);
  }

  .card--back { display: flex; align-items: center; justify-content: center; }
  .card--back .wordmark { font-size: 26px; letter-spacing: 6px; }
</style>
</head>
<body>
  <section class="card card--front">
    <div class="wordmark"><span class="wordmark__mark"></span>Velisto Events</div>
    <div class="person">
      <p class="person__name">Dana Morrowby</p>
      <p class="person__role">Director</p>
    </div>
    <div class="contact">
      <div class="contact__item">
        <p class="contact__label">Phone:</p>
        <p class="contact__value">O: 02 5147 3086<br>M: 0451 692 038</p>
      </div>
      <div class="contact__item">
        <p class="contact__label">Email:</p>
        <p class="contact__value">info@velistoevents.example.au</p>
      </div>
      <div class="contact__item">
        <p class="contact__value">www.velistoevents.example.au<br>@velistoevents</p>
      </div>
    </div>
    <div class="social">
      <span class="social__rule"></span>
      <span class="social__dot"></span>
      <span class="social__dot"></span>
      <span class="social__rule"></span>
    </div>
    <div class="gold-band gold-band--bottom"></div>
  </section>

  <section class="card card--back">
    <div class="gold-band gold-band--top"></div>
    <div class="wordmark"><span class="wordmark__mark"></span>Velisto Events</div>
    <div class="gold-band gold-band--bottom"></div>
  </section>
</body>
</html>
```